Banner Ad Design Project -Oil and Gas Value Chain

I am needing to create a simple graphic like the one here:

size: 720x300
http://craftpanelhub.example/designresources/banners/examples/720x300.php

Oil and Gas Value Chain:
The oil industry has three levels: upstream, midstream, and downstream which encompass the main segments in the supply chain. The upstream level includes the exploration, drilling, and production of crude oil and the midstream level includes the transportation and trading of crude oil to refineries. The downstream level refers to the refining of crude oil into finished product, the storage of crude oil, and the distribution and marketing of crude oil to wholesalers and retailers.

http://www.fuelvistaplan.example/images/value_chain.gif
http://www.crudelearnhub.example/modules/m008/imgs/fig_001.jpg
Here is another that is more for reference:

http://www.halvern.example/web/soc142/team9/GVC_clip_image002.jpg

https://www.findora.example/search?q=oil+value+chain&hl=en&tbo=u&prmd=imvns&tbm=isch&source=univ&sa=X&ei=I1hsUOuEC-SK2wXry4DAAg&ved=0CDMQsAQ&biw=1680&bih=925

```html
<!DOCTYPE html>
<html lang="en">
<head>
<meta charset="utf-8">
<title>Oil and Gas Value Chain</title>
<link href="https://fonts.googleapis.com/css2?family=Pathway+Gothic+One&display=swap" rel="stylesheet">
<style>
  :root {
    --ink: #000000;
    --line: #ffffff;
    --text: #ffffff;
    --art: #1c1c1c;
  }
  * { margin: 0; padding: 0; box-sizing: border-box; }
  html, body {
    width: 1200px;
    height: 504px;
    overflow: hidden;
    background: var(--ink);
  }
  .banner {
    position: relative;
    width: 1200px;
    height: 504px;
    background: var(--ink);
    color: var(--text);
    font-family: "Pathway Gothic One", "Arial Narrow", sans-serif;
    overflow: hidden;
  }
  .outlines {
    position: absolute;
    inset: 0;
    width: 1200px;
    height: 504px;
  }
  .outlines path, .outlines rect, .outlines line {
    fill: none;
    stroke: var(--line);
    stroke-width: 2;
    vector-effect: non-scaling-stroke;
  }
  .art {
    position: absolute;
    background: var(--art);
    border-radius: 4px;
  }
  .art-derrick   { left: 10px;  top: 10px;  width: 90px;  height: 225px; }
  .art-pumpjack  { left: 8px;   top: 250px; width: 167px; height: 160px; }
  .art-truck     { left: 407px; top: 17px;  width: 291px; height: 117px; }
  .art-handshake { left: 474px; top: 251px; width: 216px; height: 159px; }
  .art-refinery  { left: 828px; top: 8px;   width: 112px; height: 176px; }
  .art-barrel    { left: 1097px; top: 58px; width: 75px;  height: 109px; }
  .art-station   { left: 864px; top: 293px; width: 299px; height: 117px; }

  .stage-label {
    position: absolute;
    line-height: 1;
    white-space: nowrap;
  }
  .explore   { left: 133px; top: 88px;  font-size: 70px; }
  .drill     { left: 196px; top: 284px; font-size: 56px; }
  .drill-amp { left: 312px; top: 284px; font-size: 56px; }
  .produce   { left: 196px; top: 342px; font-size: 56px; }
  .transport {
    left: 470px; top: 138px; width: 220px;
    font-size: 46px; line-height: 0.92; text-align: center;
  }
  .refine {
    left: 948px; top: 22px; width: 116px;
    font-size: 46px; line-height: 0.95; text-align: center;
  }
  .distribute { left: 806px; top: 228px; font-size: 48px; }

  .tier-band {
    position: absolute;
    left: 0; top: 420px;
    width: 1200px; height: 84px;
  }
  .tier {
    position: absolute;
    top: 18px;
    font-size: 46px;
    line-height: 1;
  }
  .tier-up   { left: 66px; }
  .tier-mid  { left: 490px; }
  .tier-down { left: 898px; }
</style>
</head>
<body>
<main class="banner">
  <svg class="outlines" viewBox="0 0 722 301" preserveAspectRatio="none" aria-hidden="true">
    <rect x="1" y="1" width="720" height="299"/>
    <path d="M222 0 V70 C240 70 255 85 250 105 C245 125 225 120 222 140 V251"/>
    <path d="M470 0 V60 C490 60 505 80 500 100 C495 120 475 115 470 135 V251"/>
    <line x1="0" y1="251" x2="722" y2="251"/>
  </svg>

  <div class="art art-derrick" role="img" aria-label="Line drawing of an oil derrick"></div>
  <div class="art art-pumpjack" role="img" aria-label="Line drawing of an oil pumpjack"></div>
  <div class="art art-truck" role="img" aria-label="Line drawing of a tanker truck"></div>
  <div class="art art-handshake" role="img" aria-label="Two traders shaking hands over a dollar sign"></div>
  <div class="art art-refinery" role="img" aria-label="Line drawing of refinery equipment"></div>
  <div class="art art-barrel" role="img" aria-label="Line drawing of an oil barrel"></div>
  <div class="art art-station" role="img" aria-label="Line drawing of a fuel station canopy with pumps"></div>

  <span class="stage-label explore">Explore</span>
  <span class="stage-label drill">Drill</span>
  <span class="stage-label drill-amp">&amp;</span>
  <span class="stage-label produce">Produce</span>
  <span class="stage-label transport">Transport<br>&amp;<br>Trade</span>
  <span class="stage-label refine">Refine<br>&amp;<br>Store</span>
  <span class="stage-label distribute">Distribute</span>

  <footer class="tier-band">
    <span class="tier tier-up">Upstream</span>
    <span class="tier tier-mid">Midstream</span>
    <span class="tier tier-down">Downstream</span>
  </footer>
</main>
</body>
</html>
```